The most amazing design opportunity you will ever get - Plus we may even through in some shares!

We need a new look and feel for our website, something that will knock the socks off our competitors. Something fresh, functional, dynamic and awesome.

Take a look at the attached brief and see if this is something you can get you head around to come up with something just amazing.

A key to your success is to base your design on the Visual Language (colours Black with Orange on white background, integration of cogs, font, style) and remember that our target audience is BUSINESS and the key thing that we are about is INSIGHTS, so if you can include some subtle design that requires insight to use - Perfect!

```html
<!DOCTYPE html>
<html lang="en">
<head>
<meta charset="utf-8">
<title>Gearpoint Insights – Member Login</title>
<link rel="stylesheet" href="https://fonts.googleapis.com/css2?family=Oswald:wght@300;400;500&family=Raleway:wght@400;500&family=Ubuntu:wght@400;500&display=swap">
<style>
:root{
  --orange:#f7941d;
  --orange-deep:#e37c0b;
  --ink:#1d1b1c;
  --ink-soft:#2e2d2e;
  --grey-side:#e6e6e6;
  --grey-mid:#8a8a8a;
  --grey-tab:#6d6d6d;
  --white:#ffffff;
  --blue:#1f6fbf;
  --blue-light:#2f86d6;
  --pill:#3a393a;
}
*{box-sizing:border-box;margin:0;padding:0}
html,body{width:1200px;height:900px;overflow:hidden}
body{position:relative;background:var(--grey-side);font-family:"Raleway",sans-serif;color:var(--white)}
.abs{position:absolute}
.page-core{left:118px;top:0;width:966px;height:900px;background:var(--white)}

/* stats bar */
.stats-bar{left:0;top:0;width:1200px;height:45px;background:linear-gradient(#4a4a4a,#121212)}
.audience{left:124px;top:0;width:167px;height:45px;background:var(--orange)}
.toggle{display:flex;border-radius:16px;background:linear-gradient(#fdfdfd,#cfcfcf);box-shadow:inset 0 1px 3px rgba(0,0,0,.45);font-family:"Oswald",sans-serif;font-weight:300;font-size:14px;overflow:hidden;height:30px;align-items:center;padding:0 8px;gap:12px}
.toggle .off{color:#9a9a9a}
.toggle .on{color:var(--orange);font-weight:400}
.audience .toggle{position:absolute;left:20px;top:7px;width:128px}
.stat{position:absolute;top:0;height:45px;display:flex;align-items:center;gap:8px;font-family:"Oswald",sans-serif;border-left:1px solid #555;padding-left:10px}
.stat .badge{width:28px;height:28px;border-radius:50%;background:var(--orange);display:flex;align-items:center;justify-content:center}
.stat .num{color:var(--orange);font-size:15px;line-height:16px;display:block}
.stat .lbl{color:var(--white);font-size:14px;font-weight:300;line-height:16px;display:block}

/* header */
.header-panel{left:168px;top:45px;width:862px;height:150px;background:linear-gradient(90deg,#d6d6d6,#f4f4f4 55%,#dcdcdc)}
.view-toggle{left:176px;top:51px;width:125px}
.brand{left:188px;top:110px;display:flex;align-items:center;gap:8px}
.brand .dot{width:18px;height:18px;border-radius:50%;background:var(--orange)}
.brand .name{font-family:"Oswald",sans-serif;font-weight:500;font-size:40px;line-height:1;color:var(--ink);letter-spacing:.5px}
.tagline{left:398px;top:92px;font-family:"Raleway",sans-serif;font-size:21px;line-height:24.5px;color:var(--ink);text-transform:uppercase}
.ticker{left:532px;width:498px;height:30px;background:linear-gradient(#444,#141414);display:flex;align-items:center;font-family:"Oswald",sans-serif;font-weight:300;font-size:14px;color:var(--white);border-radius:0 0 4px 0}
.ticker .ico{width:28px;height:28px;border-radius:50%;background:var(--blue);margin:0 8px 0 0;display:flex;align-items:center;justify-content:center;box-shadow:0 0 0 2px #d8d8d8}

/* nav */
.nav-band{left:0;top:201px;width:265px;height:43px;background:var(--blue)}
.nav-line{left:0;top:232px;width:1200px;height:12px;background:var(--blue)}
.profile-toggle{left:130px;top:206px;width:125px}
.tab{position:absolute;top:204px;height:28px;font-family:"Oswald",sans-serif;font-size:14px;color:var(--white);display:flex;align-items:center;justify-content:center;clip-path:polygon(10px 0,calc(100% - 10px) 0,100% 100%,0 100%);border-radius:8px 8px 0 0}
.tab.home{background:var(--blue)}
.tab.dark{background:var(--pill)}
.tab.mid{background:var(--grey-tab)}
.tab.active{background:var(--orange)}
.tab.util{background:var(--blue-light)}

/* login */
.login{left:248px;top:292px;width:704px;height:426px;border-radius:95px;border:5px solid #c8c8c8;background:radial-gradient(ellipse at 55% 45%,#4b4a4b,#1e1d1e 70%)}
.login-title{left:0;top:10px;width:100%;text-align:center;font-family:"Ubuntu",sans-serif;font-weight:400;font-size:33px;color:var(--orange)}
.title-rule{left:210px;top:54px;width:280px;height:2px;background:linear-gradient(90deg,transparent,#777,transparent)}
.field-label{font-family:"Ubuntu",sans-serif;font-weight:500;font-size:13px;color:var(--white)}
.field{width:178px;height:31px;border-radius:8px;background:linear-gradient(#dcdcdc,#9b9b9b);box-shadow:0 3px 4px rgba(0,0,0,.5)}
.captcha-box{width:42px;height:33px;border-radius:9px;background:linear-gradient(#cfcfcf,#8c8c8c)}
.captcha-text{font-size:13px;color:#ddd}
.rail{left:55px;top:327px;width:280px;height:3px;background:linear-gradient(90deg,transparent,#bbb)}
.login-btn{left:186px;top:314px;width:80px;height:30px;border-radius:4px;background:linear-gradient(#ffc94a,var(--orange-deep));color:var(--ink);font-family:"Ubuntu",sans-serif;font-size:18px;text-align:center;line-height:30px}
.seal{left:268px;top:85px;width:270px;height:270px;border-radius:50%;background:#111;box-shadow:0 0 0 4px #333}
.seal-ring{left:12px;top:12px;width:246px;height:246px;border-radius:50%;background:linear-gradient(#999,#eee);border:3px solid var(--orange)}
.seal-face{left:13px;top:13px;width:214px;height:214px;border-radius:50%;background:radial-gradient(circle at 40% 30%,#fff,#e2e2e2);display:flex;align-items:center;justify-content:center;gap:6px}
.seal-face .name{font-family:"Oswald",sans-serif;font-size:34px;color:var(--ink)}
.seal-face .dot{width:16px;height:16px;border-radius:50%;background:var(--orange)}
.link-pill{height:21px;border-radius:0 11px 11px 0;background:linear-gradient(#555,#2c2c2c);font-family:"Ubuntu",sans-serif;font-size:13px;line-height:21px;padding-left:18px;color:var(--white)}
.back{left:528px;top:295px;display:flex;align-items:center;gap:6px;font-family:"Ubuntu",sans-serif;font-size:11.5px;line-height:14px}

/* footer */
.footer{left:0;top:775px;width:1200px;height:107px;background:linear-gradient(#1c1c1c,#3e3e3e)}
.foot-links{left:158px;top:16px;display:flex;gap:14px}
.foot-links span{background:#151515;border-radius:10px;padding:1px 6px;font-size:15px;color:var(--white)}
.social{top:18px;width:30px;height:28px;font-family:"Raleway",sans-serif;font-size:7px;display:flex;align-items:center;justify-content:center;color:var(--white)}
.foot-brand{left:170px;top:54px;display:flex;align-items:center;gap:12px}
.foot-brand .name{font-family:"Oswald",sans-serif;font-size:24px;color:#aaa}
.foot-brand .tag{font-size:7px;line-height:8px;color:#aaa;text-transform:uppercase}
.foot-divider{width:1px;height:34px;background:#aaa}
.contact{width:30px;height:30px;border-radius:50%;background:#a8a8a8;display:flex;align-items:center;justify-content:center}
.copyright{left:0;top:882px;width:1200px;height:18px;background:var(--blue);text-align:center;font-family:"Raleway",sans-serif;font-weight:500;font-size:10px;letter-spacing:1.5px;line-height:18px}
</style>
</head>
<body>
<div class="abs page-core"></div>

<header>
  <div class="abs stats-bar"></div>
  <div class="abs audience"><div class="toggle"><span class="off">Just Me</span><span class="on">Everyone</span></div></div>

  <div class="stat" style="left:292px"><span class="badge"><svg width="16" height="16" viewBox="0 0 16 16" fill="none" stroke="#fff" stroke-width="1.6"><circle cx="8" cy="5" r="3"/><path d="M2 15c0-4 3-6 6-6s6 2 6 6"/></svg></span><span><span class="num">3,458</span><span class="lbl">iMembers</span></span></div>
  <div class="stat" style="left:404px"><span class="badge"><svg width="16" height="16" viewBox="0 0 16 16" fill="none" stroke="#fff" stroke-width="1.6"><circle cx="8" cy="6" r="4.5"/><path d="M5 10l-2 5 3-1 2 2M11 10l2 5-3-1"/></svg></span><span><span class="num">1,700,250</span><span class="lbl">iPoints</span></span></div>
  <div class="stat" style="left:515px"><span class="badge"><svg width="16" height="16" viewBox="0 0 16 16" fill="none" stroke="#fff" stroke-width="1.6"><path d="M2 14V9h3v5M7 14V5h3v9M12 14V2h2v12"/></svg></span><span><span class="num">800,125</span><span class="lbl">iActivity</span></span></div>
  <div class="stat" style="left:624px"><span class="badge"><svg width="16" height="16" viewBox="0 0 16 16" fill="none" stroke="#fff" stroke-width="1.6"><circle cx="8" cy="8" r="6.5"/><path d="M2 8h12M8 1.5c3 3 3 10 0 13"/></svg></span><span><span class="num">600,100</span><span class="lbl">iNetworking</span></span></div>
  <div class="stat" style="left:747px"><span class="badge"><svg width="16" height="16" viewBox="0 0 16 16" fill="none" stroke="#fff" stroke-width="1.6"><path d="M2 9l7-7h5v5l-7 7z"/><circle cx="11" cy="5" r="1"/></svg></span><span><span class="num">300,025</span><span class="lbl">iAttributes</span></span></div>
  <div class="stat" style="left:862px"><span class="badge"><svg width="16" height="16" viewBox="0 0 16 16" fill="none" stroke="#fff" stroke-width="1.6"><path d="M5 2h6l-2 3c4 2 5 5 5 7 0 2-2 3-6 3s-6-1-6-3c0-2 1-5 5-7z"/></svg></span><span><span class="num">i$900,125</span><span class="lbl">iDollars</span></span></div>
  <div class="stat" style="left:977px"><span class="badge"><svg width="16" height="16" viewBox="0 0 16 16" fill="none" stroke="#fff" stroke-width="1.6"><rect x="3" y="2" width="10" height="12"/><path d="M5 5h6M5 8h6"/></svg></span><span><span class="num">900,000</span><span class="lbl">iShares</span></span></div>

  <div class="abs header-panel"></div>
  <div class="abs view-toggle toggle"><span class="off">Detail</span><span class="on">Summary</span></div>
  <div class="abs brand"><span class="name">GEARPOINT</span><span class="dot"></span></div>
  <div class="abs tagline">Business<br>Solutions<br>Through<br>Insight</div>

  <div class="abs ticker" style="top:50px"><span class="ico"><svg width="14" height="14" viewBox="0 0 14 14" fill="none" stroke="#fff" stroke-width="1.4"><path d="M2 3h10v6H6l-3 3V9H2z"/></svg></span>The Advanced Search gives you 190,000+ permutations!</div>
  <div class="abs ticker" style="top:85px"><span class="ico"><svg width="14" height="14" viewBox="0 0 14 14" fill="none" stroke="#fff" stroke-width="1.4"><path d="M4 2h6v4a3 3 0 0 1-6 0zM7 9v3M4 12h6M4 3H2c0 2 1 3 2 3M10 3h2c0 2-1 3-2 3"/></svg></span>Win i$100 for your feedback about our site</div>
  <div class="abs ticker" style="top:120px"><span class="ico"><svg width="14" height="14" viewBox="0 0 14 14" fill="none" stroke="#fff" stroke-width="1.6"><circle cx="6" cy="6" r="4"/><path d="M9 9l3.5 3.5"/></svg></span>Your Brand Ambassadors Are in the Building</div>
  <div class="abs ticker" style="top:155px"><span class="ico"><svg width="14" height="14" viewBox="0 0 14 14" fill="none" stroke="#fff" stroke-width="1.4"><circle cx="5" cy="4" r="2.5"/><path d="M1 13c0-3 2-5 4-5s4 2 4 5M11 4v4M9 6h4"/></svg></span>Dj</div>
</header>

<nav>
  <div class="abs nav-band"></div>
  <div class="abs nav-line"></div>
  <div class="abs profile-toggle toggle"><span class="off">Insights</span><span class="on">Profile</span></div>
  <div class="tab home" style="left:262px;width:72px">Home</div>
  <div class="tab dark" style="left:333px;width:130px">Business Disciplines</div>
  <div class="tab mid" style="left:467px;width:70px">Insights</div>
  <div class="tab active" style="left:535px;width:76px">Solutions</div>
  <div class="tab mid" style="left:601px;width:70px">Library</div>
  <div class="tab dark" style="left:660px;width:76px">Rewards</div>
  <div class="tab mid" style="left:728px;width:82px">Members</div>
  <div class="tab dark" style="left:802px;width:94px">Specialists</div>
  <div class="tab mid" style="left:890px;width:72px">Teams</div>
  <div class="tab util" style="left:955px;width:52px"><svg width="26" height="12" viewBox="0 0 26 12" fill="none" stroke="#fff" stroke-width="2"><circle cx="6" cy="6" r="4"/><path d="M10 6h14M20 6v4M24 6v3"/></svg></div>
  <div class="tab util" style="left:1000px;width:56px"><svg width="20" height="18" viewBox="0 0 20 18" fill="none" stroke="#fff" stroke-width="1.6"><circle cx="8" cy="5" r="3.5"/><path d="M1 17c0-4 3-7 7-7s7 3 7 7M16 3v6M13 6h6"/></svg></div>
</nav>

<main class="abs login">
  <h1 class="abs login-title">Member Login</h1>
  <div class="abs title-rule"></div>

  <label class="abs field-label" style="left:59px;top:92px">Username or Email</label>
  <div class="abs field" style="left:59px;top:113px"></div>
  <label class="abs field-label" style="left:59px;top:165px">Password</label>
  <div class="abs field" style="left:59px;top:186px"></div>
  <p class="abs field-label" style="left:60px;top:239px">Please solve this sum to sign in</p>
  <div class="abs captcha-box" style="left:59px;top:260px"></div>
  <span class="abs captcha-text" style="left:108px;top:270px">- 1= Three</span>

  <div class="abs rail"></div>
  <div class="abs login-btn">Log in</div>

  <div class="abs seal">
    <div class="abs seal-ring">
      <div class="abs seal-face"><span class="name">GEARPOINT</span><span class="dot"></span></div>
    </div>
  </div>

  <div class="abs link-pill" style="left:492px;top:120px;width:82px">Register</div>
  <div class="abs link-pill" style="left:519px;top:150px;width:158px">Forgot your Password</div>

  <div class="abs back">
    <svg width="36" height="36" viewBox="0 0 36 36" fill="none" stroke="#bbb" stroke-width="2.5"><path d="M14 4L3 16l11 12v-7c8 0 14 3 18 11 0-11-6-19-18-20z"/></svg>
    <span>Back to Gearpoint<br>Insights</span>
  </div>
</main>

<footer class="abs footer">
  <div class="abs foot-links">
    <span>Getting Started</span><span>Tutorials</span><span>Insight</span><span>Points</span><span>Index</span><span>Upcoming Topics</span><span>About us</span>
  </div>
  <span class="abs social" style="left:875px;background:#3b5998">Folio</span>
  <span class="abs social" style="left:920px;background:#2aa3ef">Chatter</span>
  <span class="abs social" style="left:963px;background:#0e76a8">Linkwork</span>
  <span class="abs social" style="left:1005px;background:#cb2027">Boardly</span>

  <div class="abs foot-brand">
    <span class="name">GEARPOINT</span>
    <span class="tag">Business<br>Solutions<br>Through<br>Insight</span>
    <span class="foot-divider"></span>
    <span class="contact"><svg width="18" height="12" viewBox="0 0 18 12" fill="#2a2a2a"><path d="M1 4c5-4 11-4 16 0l-1 3-3-1V4c-2-1-4-1-6 0v2L4 7z"/><rect x="5" y="8" width="8" height="3"/></svg></span>
    <span class="contact" aria-label="Callway"><span style="width:14px;height:14px;border-radius:50%;border:2px solid #2a2a2a"></span></span>
    <span class="contact"><svg width="16" height="12" viewBox="0 0 16 12" fill="#2a2a2a"><path d="M0 0h16v12H0z"/><path d="M0 0l8 7 8-7" stroke="#a8a8a8" stroke-width="1.4" fill="none"/></svg></span>
  </div>
</footer>
<div class="abs copyright">GEARPOINT INSIGHTS © 2014. ALL RIGHTS RESERVED.</div>
</body>
</html>
```